Business card and Stationery for data intelligence company

We need a new design for our business cards and stationery (Business Letter templates and a Quote example on Word, but it MUST work on Google Doc as well).

We are a software company based in Ireland and UK. Our product is "Quenlyx", data intelligence platform with beautiful visualizations, graph capabilities (things are interconnected), powerful, flexible, it can manage Big Data and Streaming information. It's modern and relatively open source.
Our company will provide data intelligence for law enforcements, pharmaceuticals, and similar high end customers.

We'll launch a new website soon. At the moment it's http://www.kovar-analytics.example if you want to take a look. This is our youtube channel in case you need it to understand what Quenlyx is: https://www.youtube.com/c/kovaranalyticschannel

We changed the logo so please use the logo I attach here.

We'd like the output to be cool and modern but elegant and "business" at the same time. It should inspire simple sophistication, "unity" "intent" "purpose" yet subtly very advanced and innovative.

The name "Quenlyx" does NOT refer to sirens (mithological creatures) as well as the warning devices. It means Kinetic Object Vector Analysis Reactor. Please use our logo's colors and if you want to something like the "graph" image.

```html
<!DOCTYPE html>
<html lang="en">
<head>
<meta charset="utf-8">
<title>Quenlyx – Business Card</title>
<link href="https://fonts.googleapis.com/css2?family=Montserrat:wght@500;600;700&family=Roboto:wght@400&display=swap" rel="stylesheet">
<style>
  :root {
    --bg: #2a2a2a;
    --card: #141414;
    --orange: #f7a834;
    --grey: #b9b9b9;
    --text: #d8d8d8;
  }
  * { margin: 0; padding: 0; box-sizing: border-box; }
  html, body { width: 1200px; height: 852px; overflow: hidden; background: var(--bg); }
  .canvas { position: relative; width: 1200px; height: 852px; }
  .card {
    position: absolute; width: 560px; height: 320px;
    background: var(--card); border-radius: 18px;
    box-shadow: 0 10px 30px rgba(0,0,0,.45);
    overflow: hidden;
  }
  .card--front { left: 60px; top: 80px; }
  .card--back { left: 580px; top: 452px; }

  .brand { position: absolute; display: flex; align-items: center; gap: 14px; white-space: nowrap; }
  .brand__dot { border-radius: 50%; background: var(--orange); flex: none; }
  .brand__name {
    font-family: "Montserrat", sans-serif; font-weight: 600;
    color: var(--orange); letter-spacing: 5px; line-height: 1;
  }
  .card--front .brand { left: 50%; top: 50%; transform: translate(-50%, -50%); }
  .card--front .brand__dot { width: 46px; height: 46px; }
  .card--front .brand__name { font-size: 50px; }

  .card--back .brand { left: 250px; top: 48px; gap: 10px; }
  .card--back .brand__dot { width: 30px; height: 30px; }
  .card--back .brand__name { font-size: 32px; letter-spacing: 3px; }

  .person { position: absolute; left: 40px; top: 120px; font-family: "Montserrat", sans-serif; }
  .person__name { font-size: 19px; font-weight: 700; color: var(--text); text-transform: uppercase; line-height: 1.1; }
  .person__role { font-size: 11.5px; font-weight: 600; color: var(--orange); text-transform: uppercase; letter-spacing: .3px; }

  .address {
    position: absolute; right: 40px; top: 118px; text-align: right;
    font-family: "Roboto", sans-serif; font-style: normal; font-size: 13px;
    color: var(--text); line-height: 1.45;
  }

  .contacts { position: absolute; left: 40px; bottom: 30px; list-style: none;
    font-family: "Roboto", sans-serif; font-size: 14px; color: var(--text); }
  .contacts li { display: flex; align-items: center; gap: 8px; line-height: 22px; }
  .contacts svg { width: 14px; height: 14px; flex: none; }
</style>
</head>
<body>
<main class="canvas">
  <section class="card card--front" aria-label="Card front">
    <div class="brand">
      <span class="brand__dot"></span>
      <span class="brand__name">QUENLYX</span>
    </div>
  </section>

  <section class="card card--back" aria-label="Card back">
    <div class="brand">
      <span class="brand__dot"></span>
      <span class="brand__name">QUENLYX</span>
    </div>

    <div class="person">
      <p class="person__name">Daniel Marsh</p>
      <p class="person__role">Managing Director</p>
    </div>

    <address class="address">Lakeside 214 Harbour Road<br>Cork T12 4400</address>

    <ul class="contacts">
      <li>
        <svg viewBox="0 0 14 14" aria-hidden="true"><circle cx="7" cy="7" r="7" fill="#f7a834"/><path d="M4.5 3.6l1.2-.2.7 1.7-.8.6c.4.9 1 1.5 1.9 1.9l.6-.8 1.7.7-.2 1.2c-2.8.2-5.3-2.3-5.1-5.1z" fill="#141414"/></svg>
        07700900155
      </li>
      <li>
        <svg viewBox="0 0 14 14" aria-hidden="true"><circle cx="7" cy="7" r="7" fill="#f7a834"/><rect x="3.5" y="4.5" width="7" height="5" fill="#141414"/><path d="M3.5 4.5L7 7.3l3.5-2.8" stroke="#f7a834" stroke-width=".8" fill="none"/></svg>
        name@quenlyx-analytics.example
      </li>
      <li>
        <svg viewBox="0 0 14 14" aria-hidden="true"><circle cx="7" cy="7" r="7" fill="#f7a834"/><g stroke="#141414" stroke-width=".8" fill="none"><circle cx="7" cy="7" r="3.6"/><ellipse cx="7" cy="7" rx="1.5" ry="3.6"/><path d="M3.4 7h7.2"/></g></svg>
        www.quenlyx-analytics.example
      </li>
    </ul>
  </section>
</main>
</body>
</html>
```